K&R Flame Guard Supply Inc. needs an updated/new website design

I would like the customer to be able to see who we are, where are are, what we do and areas we cover on the first page. I would like something modern but professional. The other fire safety companies out there have very boring & unappealing websites. I want mine seem like we've got it together and to be above average in comparison. I would like the colors to go with our logo and would like to incorporate somewhere that we have been in business for over 30 years, we are family owned and operated and that we provide service to all of central Florida from Tampa to Titusville and all of Brevard county (we can take out the" all of Brevard county" but keep the " All of Central Florida from Tampa to Titusville" and just add all counties we service to the very bottom too). We are a residential and commercial fire safety equipment company. We do sales, service and installation for fire extinguishers, emergency/exit lighting, kitchen fire suppression systems, fire alarms & fire extinguisher cabinets.I have also attached some pictures that you can use to incorporate any way you would like. Here's our current website (awful I know) to get information from if needed. kandrflameguard.example

Target Market(s)

Restaurants, hotels, vacation rental properties & small businesses. Every business is required to have a fire extinguisher and exit lighting.

Industry/Entity Type

Fire Safety

Number of Pages Required

1 page

Font styles to use
Other font styles liked:
• I'm open to your suggestions

Colors

Designer to choose colors to be used in the design.

Requirements
Must have
• I would like the customer to be able to see who we are, where are are, what we do and areas we cover on the first page. I would like the colors to go with our logo and would like to incorporate somewhere that we have been in business for over 30 years, we are family owned and operated and that we provide service to all of central Florida from Tampa to Titusville and all of Brevard county (we can take out the" all of Brevard county" but keep the " All of Central Florida from Tampa to Titusville" and just add all counties we service to the very bottom too)
Nice to have
• Modern with high quality pictures
• I love the raised logo that I added in the attachments. If you could make the logo look like that in incorporate it as one of the first things you see that would be awesome!
• I would eventually like to have a portfolio of work completed on an additional page.
Should not have
• boring outdated look

```html
<!DOCTYPE html>
<html lang="en">
<head>
<meta charset="utf-8">
<title>K&amp;R Flame Guard Supply Inc.</title>
<link href="https://fonts.googleapis.com/css2?family=Lato:wght@400;700&display=swap" rel="stylesheet">
<style>
:root{
  --orange:#fbb055;
  --orange-deep:#f7941d;
  --ink:#222;
  --text:#333;
  --gray-bg:#efefef;
  --white:#fff;
  --blue:#1e73be;
  --quote:#9fb6cc;
}
*{box-sizing:border-box;margin:0;padding:0}
html,body{width:1130px;height:1200px;overflow:hidden}
body{font-family:"Lato",sans-serif;color:var(--text);background:var(--white);position:relative}
.abs{position:absolute}

/* hero */
.hero{left:0;top:0;width:1130px;height:282px;
  background:linear-gradient(90deg,#8a6a3a 0%,#b58a4a 25%,#8e8a7e 50%,#4e7aa0 75%,#2d5f8e 100%)}
.hero-shade{left:0;top:0;width:1130px;height:282px;background:linear-gradient(180deg,rgba(0,0,0,.15),rgba(0,0,0,0) 50%,rgba(0,0,0,.1))}
.brand{left:142px;top:22px;width:120px;color:var(--white);font-weight:700;font-size:15px;line-height:18px;display:flex;align-items:center;gap:8px}
.brand i{display:block;width:14px;height:14px;border-radius:50%;background:var(--orange-deep);flex:none}
.nav{left:0;top:35px;width:987px;display:flex;justify-content:flex-end;gap:36px;font-size:13px;color:var(--white)}
.nav .active{color:var(--orange-deep)}
.nav-rule{left:141px;top:85px;width:847px;height:1px;background:rgba(255,255,255,.6)}
.nav-mark{left:553px;top:84px;width:70px;height:2px;background:var(--orange-deep)}
.headline{left:0;top:128px;width:1130px;text-align:center;color:var(--white);font-size:22px;font-weight:700}
.subline{left:0;top:162px;width:1130px;text-align:center;color:var(--white);font-size:15px;font-weight:700}
.subline span{color:var(--orange-deep)}
.search{left:442px;top:207px;width:247px;height:28px;background:var(--white);border-radius:2px}
.search-btn{left:640px;top:207px;width:49px;height:28px;background:var(--orange-deep);display:flex;align-items:center;justify-content:center}

/* highlights */
.band-gray{left:0;top:282px;width:1130px;height:253px;background:var(--gray-bg)}
.card{width:272px;height:120px;background:var(--white);top:351px}
.card-head{height:18px;background:var(--orange);color:var(--white);font-size:10.5px;font-weight:700;text-align:center;line-height:18px}
.card-body{display:flex;gap:12px;padding:8px 12px 0 15px}
.card-text{font-size:7.4px;line-height:14px;color:var(--ink);width:160px}
.card-text a{color:var(--orange-deep);text-decoration:none}
.card-pic{width:77px;height:75px;background:var(--orange);font-size:7.5px;display:flex;align-items:center;justify-content:center;text-align:center;line-height:15px;color:var(--ink);margin-top:4px}
.card-map{width:115px;height:72px;background:linear-gradient(90deg,#a9d6f5 55%,#f3ead8 55%);margin-left:auto;margin-top:6px}
.card-icon{top:293px;height:62px;width:70px;border-radius:8px}

/* products */
.tabs{left:0;top:535px;width:1130px;height:32px;background:var(--orange)}
.tab-list{left:142px;top:532px;display:flex;font-size:14px;color:var(--white);height:35px;align-items:center}
.tab-list span{padding:0 13px}
.tab-list .on{background:var(--orange-deep);font-weight:700;height:35px;line-height:35px;padding:0 12px}
.provide-title{left:157px;top:576px;font-size:14px;color:var(--ink)}
.provide-list{left:157px;top:607px;list-style:none;font-size:11px;color:var(--ink)}
.provide-list li{display:flex;align-items:center;gap:14px;height:28.5px}
.lorem-title{left:378px;top:576px;font-size:14px;color:var(--ink)}
.lorem-copy{left:370px;top:610px;width:400px;text-align:center;font-size:10.5px;line-height:24px;color:var(--ink)}
.tech-photo{left:834px;top:574px;width:150px;height:172px;background:linear-gradient(160deg,#e8e8e8,#7a7f88 60%,#4a4e56)}

/* testimonials */
.band-test{left:0;top:763px;width:1130px;height:202px;background:var(--gray-bg)}
.test-title{left:368px;top:773px;font-size:21px;font-weight:700;color:var(--ink)}
.quote-text{left:226px;top:827px;width:412px;text-align:center;font-size:10px;letter-spacing:.2px;line-height:25.5px;color:var(--ink)}
.quote-open,.quote-close{font-size:60px;color:var(--quote);font-weight:700;line-height:1}
.quote-open{left:190px;top:808px}
.quote-close{left:628px;top:900px}
.avatar{left:791px;top:810px;width:92px;height:92px;border-radius:50%;background:linear-gradient(180deg,#6b6d70,#3d3f42)}
.person{left:737px;top:906px;width:200px;text-align:center;font-size:13.5px;color:var(--orange-deep)}
.role{left:737px;top:924px;width:200px;text-align:center;font-size:9.5px;color:var(--ink)}
.dots{left:808px;top:940px;display:flex;gap:8px}
.dots i{width:9px;height:9px;border-radius:50%;border:2px solid var(--orange-deep);display:block}
.dots i.on{background:var(--blue)}

/* footer */
.footer{left:0;top:965px;width:1130px;height:235px;background:var(--orange)}
.foot-h{top:979px;font-size:12.5px;font-weight:700;color:var(--white)}
.quick{left:206px;top:1000px;list-style:none;font-size:10px;color:var(--white);line-height:21px}
.socials{left:457px;top:1034px;display:flex;gap:13px}
.socials span{width:30px;height:30px;border-radius:50%;background:var(--blue);display:flex;align-items:center;justify-content:center}
.email{left:727px;top:1014px;width:212px;height:21px;background:var(--white);border-radius:2px;font-size:9px;color:#999;padding:5px 14px}
.signup{left:727px;top:1050px;width:70px;height:20px;background:var(--blue);color:var(--white);font-size:10px;text-align:center;line-height:20px;border-radius:2px}
.foot-brand{left:480px;top:1110px;width:170px;justify-content:center;color:var(--white);font-weight:700;font-size:14px;text-align:center;display:flex;align-items:center;gap:8px}
.foot-brand i{display:block;width:12px;height:12px;border-radius:50%;background:var(--orange-deep);flex:none}
</style>
</head>
<body>

<div class="abs hero" role="img" aria-label="Blurred city skyline reflected on a lake at dusk"></div>
<div class="abs hero-shade"></div>
<div class="abs brand"><i></i>K&amp;R Flame Guard Supply Inc.</div>
<nav class="abs nav"><span class="active">Home</span><span>About Us</span><span>Our Products</span><span>Services</span><span>Contact</span></nav>
<div class="abs nav-rule"></div>
<div class="abs nav-mark"></div>
<h1 class="abs headline">Sales, Service, Instalation</h1>
<p class="abs subline">How can we help <span>You?</span></p>
<div class="abs search"></div>
<div class="abs search-btn"><svg width="16" height="16" viewBox="0 0 16 16"><circle cx="6.5" cy="6.5" r="4.8" fill="none" stroke="#222" stroke-width="2"/><line x1="10" y1="10" x2="15" y2="15" stroke="#222" stroke-width="2.4" stroke-linecap="round"/></svg></div>

<div class="abs band-gray"></div>
<div class="abs card-icon" style="left:142px;background:#e9a56b" role="img" aria-label="Family illustration"></div>
<div class="abs card-icon" style="left:428px;width:50px;background:#f36f21" role="img" aria-label="Flame illustration"></div>
<div class="abs card-icon" style="left:720px;width:68px;background:#2c3e5a" role="img" aria-label="Road with location pins illustration"></div>

<section class="abs card" style="left:142px">
  <div class="card-head">Family owned company</div>
  <div class="card-body">
    <p class="card-text">Lorem ipsum dolor sit amet, consectetur adipiscing elit, sed do eiusmod tempor incididunt ut labore et dolore magna aliqua. Ut enim ad minim veniam, quis nostrud exercitation ullamco laboris nisi <a>Learn more...</a></p>
    <div class="card-pic">Picture of<br>your team</div>
  </div>
</section>
<section class="abs card" style="left:429px">
  <div class="card-head">Over 30 years of experience</div>
  <div class="card-body">
    <p class="card-text">Lorem ipsum dolor sit amet, consectetur adipiscing elit, sed do eiusmod tempor incididunt ut labore et dolore magna aliqua. Ut enim ad minim veniam, quis nostrud exercitation ullamco laboris nisi <a>Learn more...</a></p>
    <div class="card-pic">Picture</div>
  </div>
</section>
<section class="abs card" style="left:716px">
  <div class="card-head">Wide range of service</div>
  <div class="card-body">
    <p class="card-text" style="width:120px">we provide service to all of central Florida from Tampa to Titusville and all of Brevard county<br><a>Learn more...</a></p>
    <div class="card-map" role="img" aria-label="Map of central Florida"></div>
  </div>
</section>

<div class="abs tabs"></div>
<div class="abs tab-list"><span class="on">Extinguishers</span><span>Emergency Exit Signs</span><span>Fire Supression Systems</span><span>Fire Alarms</span></div>
<h2 class="abs provide-title" style="font-weight:400">We provide following:</h2>
<ul class="abs provide-list">
  <li><svg width="16" height="20" viewBox="0 0 16 20"><path d="M8 1C9 6 15 8 14 14a6 6 0 0 1-12 0C2 10 5 9 5 5c2 2 3 3 3 5 1-3 1-6 0-9z" fill="#f36f21"/></svg>ABC Extinguishers</li>
  <li><svg width="16" height="20" viewBox="0 0 16 20"><path d="M8 1C9 6 15 8 14 14a6 6 0 0 1-12 0C2 10 5 9 5 5c2 2 3 3 3 5 1-3 1-6 0-9z" fill="#f36f21"/></svg>CO2 Extinguishers</li>
  <li><svg width="16" height="20" viewBox="0 0 16 20"><path d="M8 1C9 6 15 8 14 14a6 6 0 0 1-12 0C2 10 5 9 5 5c2 2 3 3 3 5 1-3 1-6 0-9z" fill="#f36f21"/></svg>K-Class Extinguishers</li>
  <li><svg width="16" height="20" viewBox="0 0 16 20"><path d="M8 1C9 6 15 8 14 14a6 6 0 0 1-12 0C2 10 5 9 5 5c2 2 3 3 3 5 1-3 1-6 0-9z" fill="#f36f21"/></svg>Halon Extinguishers</li>
</ul>
<h2 class="abs lorem-title" style="font-weight:400">Lorem Ipsum</h2>
<p class="abs lorem-copy">Lorem ipsum dolor sit amet, consectetur adipiscing elit, sed do eiusmod tempor incididunt ut labore et dolore magna aliqua. Ut enim ad minim veniam, quis nostrud exercitation ullamco laboris nisi ut aliquip ex ea commodo consequat.</p>
<div class="abs tech-photo" role="img" aria-label="Technician inspecting a fire extinguisher cabinet"></div>

<div class="abs band-test"></div>
<h2 class="abs test-title">Testimonials</h2>
<div class="abs quote-open">“</div>
<p class="abs quote-text">Lorem ipsum dolor sit amet, consectetur adipiscing elit, sed do eiusmod tempor incididunt ut labore et dolore magna aliqua. Ut enim ad minim veniam, quis nostrud exercitation ullamco laboris nisi ut aliquip ex ea commodo consequat. Duis aute irure dolor in reprehenderit in voluptate velit esse cillum dolore eu fugiat nulla pariatur.</p>
<div class="abs quote-close">”</div>
<div class="abs avatar" role="img" aria-label="Customer portrait"></div>
<div class="abs person">Dan Hollis</div>
<div class="abs role">Carpenter in Birchline Co.</div>
<div class="abs dots"><i class="on"></i><i></i><i></i><i></i></div>

<footer class="abs footer"></footer>
<h3 class="abs foot-h" style="left:191px">Quick Menu</h3>
<ul class="abs quick"><li>Home</li><li>About Us</li><li>Our Products</li><li>Services</li><li>Contact</li></ul>
<h3 class="abs foot-h" style="left:458px">Follow Us</h3>
<div class="abs socials">
  <span aria-label="Social network"></span>
  <span aria-label="Social network"></span>
  <span aria-label="Video channel"><svg width="10" height="10" viewBox="0 0 10 10"><path d="M2 1l7 4-7 4z" fill="#fff"/></svg></span>
  <span aria-label="Email"><svg width="16" height="12" viewBox="0 0 16 12"><rect x="1" y="1" width="14" height="10" rx="1" fill="#fff"/><path d="M1 1l7 6 7-6" fill="none" stroke="#1e73be" stroke-width="1.4"/></svg></span>
</div>
<h3 class="abs foot-h" style="left:727px">Sign Up for a Newsletter</h3>
<div class="abs email">Your Email Address</div>
<div class="abs signup">SIGN UP</div>
<div class="abs foot-brand"><i></i>K&amp;R Flame Guard Supply Inc.</div>

</body>
</html>
```